New young doctors office business card

Doctor's office
Hello:
My name is Dr. Mateo Anselmo Quiroga Benítez. I need a business card for my new office located within a hospital. The name of the hospital is "Hospital Almendral". Although the hospital logo and name must be included in the business card, please make me a personal logo for myself. The logo might be maybe my name in a stylish font, or my initials (MAQB) or something like that. Im more inclined to a font logo, rather than a image logo, but a good one might change my mind. The info on my business card is going to be in spanish. The following info must be included please (the info within parenthesis is not to be included, it is provided for you to understand it since it's in spanish, so you can properly place it on the card):
-Dr. Mateo Anselmo Quiroga Benítez (my name)
-Medicina general (My specialty)
-Hospital Almendral (The name of the hospital where my office is)
-Calle Tomás Ibarrola #527 Col. Peñascal (address)
-Tel 471-5836 (Office phone)
-Sábado y domingo 10:00 am a 10:00pm (Office hours)
-Emergencias: 613-907-5148 (Emergency phone)
-mateoqb@correoandino.net (email)
-English Spoken
So, that's all the info i need to be on the business card. Although it's a business card for a doctor's office, i dont want it to be a boring, plain business card. Make it eye-catchy and stylish please. As i said, the hospital logo must be included. You'll find it on the heading of the PDF file i attached, but dont make it the center of attention.
Physician
Hello:My name is Dr. Mateo Anselmo Quiroga Benítez. I need a business card for my new office located within a hospital. The name of the hospital is "Hospital Almendral". Although the hospital logo and name must be included in the business card, please make me a personal logo for myself. The logo might be maybe my name in a stylish font, or my initials (MAQB) or something like that. Im more inclined to a font logo, rather than a image logo, but a good one might change my mind. The info on my business card is going to be in spanish. The following info must be included please (the info within parenthesis is not to be included, it is provided for you to understand it since it's in spanish, so you can properly place it on the card):-Dr. Mateo Anselmo Quiroga Benítez (my name)-Medicina general (My specialty)-Hospital Almendral (The name of the hospital where my office is)-Calle Tomás Ibarrola #527 Col. Peñascal (address)-Tel 471-5836 (Office phone)-Sábado y domingo 10:00 am a 10:00pm (Office hours)-Emergencias: 613-907-5148 (Emergency phone)-mateoqb@correoandino.net (email)-English Spoken So, that's all the info i need to be on the business card. Although it's a business card for a doctor's office, i dont want it to be a boring, plain business card. Make it eye-catchy and stylish please. As i said, the hospital logo must be included. You'll find it on the heading of the PDF file i attached, but dont make it the center of attention.

```html
<!DOCTYPE html>
<html lang="es">
<head>
<meta charset="utf-8">
<title>Tarjeta de presentación — Dr. Mateo Anselmo Quiroga Benítez</title>
<link rel="stylesheet" href="https://fonts.googleapis.com/css2?family=PT+Sans:wght@400;700&family=PT+Sans+Narrow:wght@700&display=swap">
<style>
  :root {
    --page-bg: #e9e6e1;
    --card-white: #ffffff;
    --card-orange: #fb3c14;
    --brand-blue: #1f3a9c;
    --brand-red: #e8201f;
    --accent-red: #f0341c;
    --ink: #1b1b1b;
    --rule: #111111;
  }
  * { box-sizing: border-box; margin: 0; padding: 0; }
  html, body {
    width: 1200px; height: 918px; overflow: hidden;
    background: var(--page-bg);
    font-family: "PT Sans", "Myriad Pro", sans-serif;
  }
  .canvas {
    position: relative; width: 1200px; height: 918px;
    display: flex; flex-direction: column; align-items: center; justify-content: center; gap: 38px;
  }
  .card {
    position: relative; width: 700px; height: 400px;
    box-shadow: 0 6px 18px rgba(0,0,0,0.18);
  }
  /* front */
  .card-front { background: var(--card-white); color: var(--ink); }
  .personal-mark {
    position: absolute; left: 40px; top: 60px;
    display: flex; align-items: center; gap: 12px;
  }
  .personal-mark .mark-square { width: 30px; height: 30px; background: var(--brand-red); }
  .personal-mark .mark-name {
    font-family: "PT Sans", sans-serif; font-weight: 700; font-size: 58px;
    color: var(--brand-blue); letter-spacing: 1px; line-height: 1;
  }
  .hospital-mark {
    position: absolute; right: 34px; top: 44px; width: 150px;
    font-weight: 700; font-size: 22px; line-height: 1.05; text-align: right;
    color: var(--brand-blue);
  }
  .doctor-heading { position: absolute; left: 228px; top: 150px; width: 440px; }
  .doctor-name {
    font-family: "PT Sans Narrow", sans-serif; font-weight: 700; font-size: 27px;
    color: var(--ink); white-space: nowrap; line-height: 1.1;
  }
  .doctor-specialty { font-size: 22px; color: var(--ink); line-height: 1.1; }
  .heading-rule { position: absolute; left: 218px; top: 212px; width: 450px; height: 2px; background: var(--rule); }
  .contact-block { position: absolute; left: 150px; top: 228px; display: flex; gap: 10px; }
  .contact-icons { display: flex; flex-direction: column; gap: 13px; padding-top: 4px; width: 30px; align-items: center; }
  .contact-divider { width: 3px; background: var(--brand-red); }
  .contact-text { font-size: 18px; line-height: 1.22; color: var(--ink); }
  .contact-text .hospital-name { font-size: 27px; color: var(--accent-red); line-height: 1.05; }
  .card-footer {
    position: absolute; left: 150px; right: 34px; bottom: 26px;
    display: flex; justify-content: space-between; align-items: flex-end; font-size: 19px;
  }
  .office-hours { color: var(--accent-red); }
  .language-note { color: var(--ink); }
  /* back */
  .card-back { background: var(--card-orange); color: var(--card-white); }
  .back-mark {
    position: absolute; left: 0; right: 0; top: 110px; text-align: center;
    font-weight: 700; font-size: 96px; letter-spacing: 4px; color: var(--card-white);
  }
  .back-name {
    position: absolute; left: 0; right: 0; bottom: 70px; text-align: center;
    font-family: "PT Sans Narrow", sans-serif; font-weight: 700; font-size: 26px;
  }
</style>
</head>
<body>
<main class="canvas">
  <section class="card card-front" aria-label="Anverso de la tarjeta">
    <div class="personal-mark">
      <span class="mark-square"></span>
      <span class="mark-name">MAQB</span>
    </div>
    <div class="hospital-mark">Hospital Almendral</div>

    <div class="doctor-heading">
      <p class="doctor-name">Dr. Mateo Anselmo Quiroga Benítez</p>
      <p class="doctor-specialty">Medicina general</p>
    </div>
    <div class="heading-rule"></div>

    <div class="contact-block">
      <div class="contact-icons">
        <svg width="20" height="26" viewBox="0 0 20 26" aria-label="Dirección">
          <path d="M10 1a8 8 0 0 0-8 8c0 6 8 15 8 15s8-9 8-15a8 8 0 0 0-8-8z" fill="none" stroke="#111" stroke-width="2"/>
          <circle cx="10" cy="9" r="3" fill="#111"/>
        </svg>
        <svg width="22" height="24" viewBox="0 0 22 24" aria-label="Teléfono">
          <path d="M6 2l4 5-3 3c1 3 4 6 7 7l3-3 4 4-3 4C10 22 2 13 2 5z" fill="#111"/>
        </svg>
        <svg width="26" height="18" viewBox="0 0 26 18" aria-label="Correo">
          <rect x="1" y="1" width="24" height="16" fill="none" stroke="#111" stroke-width="2"/>
          <path d="M1 1l12 9 12-9" fill="none" stroke="#111" stroke-width="2"/>
        </svg>
      </div>
      <div class="contact-divider"></div>
      <div class="contact-text">
        <p class="hospital-name">Hospital Almendral</p>
        <p>Calle Tomás Ibarrola #527 Col. Peñascal</p>
        <p>613-471-5836 (Office)</p>
        <p>613-907-5148 (Emergency)</p>
        <p>mateoqb@correoandino.net</p>
      </div>
    </div>

    <div class="card-footer">
      <span class="office-hours">Sábado y domingo 10.00am a 10.00pm</span>
      <span class="language-note">English Spoken</span>
    </div>
  </section>

  <section class="card card-back" aria-label="Reverso de la tarjeta">
    <div class="back-mark">MAQB</div>
    <p class="back-name">Dr. Mateo Anselmo Quiroga Benítez</p>
  </section>
</main>
</body>
</html>
```